Kitchen and custom cabinetry company looking for business card design

We make: * Custom Kitchens, contemporary and traditional kitchens, Vanities, Libraries, Custom Entry Doors, Custom Wine Cellars and Custom Design Furniture. Phone number 555-318-2746. Address: Maple Cove NY. Email: BRAVOK@mailbox.example Portfolio at: BRAVOKcabinetry.example I would like moderns fonts and not heavy lines. double side but maybe will use clear plastic. I attached the logo.

```html
<!DOCTYPE html>
<html lang="en">
<head>
<meta charset="utf-8">
<title>Bravok Cabinetry Inc. – Business Card</title>
<link rel="stylesheet" href="https://fonts.googleapis.com/css2?family=Questrial&family=Fira+Sans:ital,wght@1,300&display=swap">
<style>
  :root {
    --backdrop: #ecebea;
    --card: #ffffff;
    --ink-grey: #6f6f6f;
    --ink-soft: #8a8a8a;
    --rule: #b5b5b5;
    --accent: #f26522;
  }
  * { box-sizing: border-box; margin: 0; padding: 0; }
  html, body {
    width: 900px;
    height: 1200px;
    overflow: hidden;
    background: var(--backdrop);
  }
  .sheet {
    position: relative;
    width: 900px;
    height: 1200px;
    display: flex;
    flex-direction: column;
    align-items: center;
    justify-content: center;
    gap: 110px;
  }
  .card {
    width: 630px;
    height: 360px;
    background: var(--card);
    box-shadow: 0 6px 22px rgba(0,0,0,0.12);
    display: flex;
    flex-direction: column;
    align-items: center;
    justify-content: center;
    color: var(--ink-grey);
  }
  /* Back side: contact details */
  .card-back {
    font-family: "Questrial", sans-serif;
    gap: 18px;
    text-align: center;
  }
  .contact-line { font-size: 17px; color: var(--ink-soft); letter-spacing: 0.3px; white-space: nowrap; }
  .contact-line .label { font-style: italic; color: var(--ink-grey); }
  .contact-phone { font-size: 26px; }
  .contact-phone .label { font-size: 22px; }
  .contact-place { font-size: 16px; color: var(--ink-grey); letter-spacing: 0.6px; margin-top: 6px; }

  /* Front side: company name and offering */
  .card-front { padding: 0 40px; }
  .company {
    display: flex;
    align-items: center;
    gap: 14px;
    font-family: "Questrial", sans-serif;
    font-weight: 400;
    font-size: 31px;
    letter-spacing: 2px;
    color: var(--ink-grey);
    white-space: nowrap;
  }
  .company-mark {
    width: 22px;
    height: 22px;
    background: var(--accent);
    flex: none;
  }
  .divider {
    width: 470px;
    height: 1px;
    background: var(--rule);
    margin: 26px 0 12px;
  }
  .offering {
    font-family: "Fira Sans", sans-serif;
    font-style: italic;
    font-weight: 300;
    font-size: 24px;
    color: var(--ink-grey);
    white-space: nowrap;
  }
</style>
</head>
<body>
  <main class="sheet">
    <section class="card card-back" aria-label="Card back">
      <p class="contact-line contact-phone"><span class="label">Phone:</span> 555-318-2746</p>
      <p class="contact-line"><span class="label">eMail</span> BRAVOK@mailbox.example</p>
      <p class="contact-line"><span class="label">Portfolio:</span> BRAVOKcabinetry.example</p>
      <p class="contact-place">Maple Cove NY</p>
    </section>

    <section class="card card-front" aria-label="Card front">
      <h1 class="company"><span class="company-mark" aria-hidden="true"></span>BRAVOK CABINETRY INC.</h1>
      <div class="divider"></div>
      <p class="offering">Custom kitchens, Vanities, Libraries, and more.</p>
    </section>
  </main>
</body>
</html>
```